Advertisement Design

I'm looking for a post card sized advertisement piece that I will be dropping off to commercial and residential customers.
On one side I want it promoting carpet cleaning services and on the other side dryer vent cleaning services.
I've uploaded two different layouts of my company logo for you to choice from.
One batch will be printed with my Michigan Number
One batch will be printed with my Tennessee number
Will share contact numbers with the winner so just use a make up number
555-318-4729

```html
<!DOCTYPE html>
<html lang="en">
<head>
<meta charset="utf-8">
<title>Fiberway – Carpet Cleaning Postcard</title>
<link rel="stylesheet" href="https://fonts.googleapis.com/css2?family=Montserrat:wght@400;500;600;700;800&display=swap">
<style>
  :root {
    --page-bg: #ececec;
    --white: #ffffff;
    --brand-blue: #0f7cc6;
    --deep-blue: #0c4ea6;
    --sky-blue: #45b8f0;
    --band-gray: #56585c;
    --soft-gray: #cfd3d8;
    --photo-teal: #3fa6bb;
    --photo-light: #d9d9d6;
    --badge-dark: #3b3d42;
  }
  * { margin: 0; padding: 0; box-sizing: border-box; }
  html, body { width: 1200px; height: 900px; overflow: hidden; background: var(--page-bg); }
  body { font-family: "Montserrat", sans-serif; }

  .postcard {
    position: absolute; left: 20px; top: 38px;
    width: 1160px; height: 824px;
    background: var(--white);
    overflow: hidden;
    box-shadow: 0 2px 10px rgba(0,0,0,.12);
  }
  .postcard-art { position: absolute; inset: 0; }

  .brand { position: absolute; left: 76px; top: 38px; width: 310px; text-align: center; }
  .brand-mark { width: 80px; height: 80px; margin: 0 auto 16px; background: var(--brand-blue); border-radius: 10px; }
  .brand-name { font-weight: 600; font-size: 42px; letter-spacing: 1px; color: var(--brand-blue); line-height: 1; }

  .headline {
    position: absolute; left: 59px; top: 282px;
    font-weight: 800; font-size: 70px; line-height: 66px;
    color: var(--white); letter-spacing: .5px;
  }
  .intro {
    position: absolute; left: 59px; top: 438px; width: 570px;
    font-weight: 400; font-size: 20.5px; line-height: 27.5px; color: var(--white);
  }

  .services { position: absolute; list-style: none; color: var(--white); font-weight: 700; font-size: 24.5px; }
  .services li { position: relative; padding-left: 34px; line-height: 30px; }
  .services li svg { position: absolute; left: 0; top: 5px; width: 22px; height: 22px; }
  .services-left { left: 54px; top: 563px; }
  .services-left li { margin-bottom: 6.5px; }
  .services-right { left: 520px; top: 577px; }
  .services-right li { margin-bottom: 6px; }

  .footer-tagline {
    position: absolute; left: 30px; top: 752px; width: 414px; text-align: center;
    font-weight: 600; font-size: 26px; line-height: 30px; color: var(--deep-blue);
  }
  .quote-cta {
    position: absolute; left: 478px; top: 752px; width: 232px; text-align: center;
    font-weight: 500; font-size: 24.5px; line-height: 29px; color: var(--sky-blue);
  }
  .cta-divider { position: absolute; left: 717px; top: 740px; width: 2px; height: 68px; background: var(--white); }
  .call {
    position: absolute; left: 736px; top: 746px;
    font-weight: 700; font-size: 38px; line-height: 40px; color: var(--white); white-space: nowrap;
  }
  .call span { margin-right: 12px; }
  .website {
    position: absolute; left: 766px; top: 786px;
    font-weight: 500; font-size: 23px; line-height: 28px; color: var(--white); letter-spacing: .5px;
    display: flex; align-items: center; gap: 6px;
  }
  .website svg { width: 18px; height: 18px; }
</style>
</head>
<body>
<main class="postcard">
  <svg class="postcard-art" viewBox="0 0 1160 824" width="1160" height="824" aria-hidden="false">
    <defs>
      <linearGradient id="hero-tones" x1="0" y1="0" x2="0" y2="1">
        <stop offset="0" stop-color="#e4e4e2"/>
        <stop offset=".32" stop-color="#cfd0cf"/>
        <stop offset=".45" stop-color="#55b3c6"/>
        <stop offset="1" stop-color="#2f93ab"/>
      </linearGradient>
      <linearGradient id="rug-tones" x1="0" y1="0" x2="1" y2="1">
        <stop offset="0" stop-color="#3c4f8a"/>
        <stop offset=".55" stop-color="#cfccc4"/>
        <stop offset="1" stop-color="#efe9dc"/>
      </linearGradient>
      <linearGradient id="sofa-tones" x1="0" y1="0" x2="1" y2="1">
        <stop offset="0" stop-color="#b9a23e"/>
        <stop offset=".45" stop-color="#3c3a3e"/>
        <stop offset="1" stop-color="#55525a"/>
      </linearGradient>
      <linearGradient id="stain-tones" x1="0" y1="0" x2="0" y2="1">
        <stop offset="0" stop-color="#ebe6dc"/>
        <stop offset=".6" stop-color="#d9d1c2"/>
        <stop offset="1" stop-color="#bfae94"/>
      </linearGradient>
    </defs>

    <!-- hero photo area -->
    <g role="img" aria-label="Photo: carpet extraction wand cleaning a teal shag rug in front of a white sofa">
      <path d="M500 0 H1160 V600 H470 C450 380 450 150 500 0 Z" fill="url(#hero-tones)"/>
    </g>
    <path d="M478 0 C448 120 444 250 470 380" fill="none" stroke="var(--brand-blue)" stroke-width="7"/>

    <!-- lower blue panel with gray edge band -->
    <path d="M0 244 C140 206 320 204 450 262 C600 330 800 480 1160 496 V824 H0 Z" fill="var(--band-gray)"/>
    <path d="M0 262 C140 226 320 224 446 282 C596 350 800 500 1160 514 V824 H0 Z" fill="var(--brand-blue)"/>

    <!-- service photo circles -->
    <circle cx="517" cy="276" r="124" fill="var(--white)"/>
    <circle cx="517" cy="276" r="117" fill="url(#rug-tones)" role="img" aria-label="Photo: technician in gloves cleaning a white rug with a hand tool"/>
    <circle cx="742" cy="426" r="124" fill="var(--white)"/>
    <circle cx="742" cy="426" r="117" fill="url(#sofa-tones)" role="img" aria-label="Photo: upholstery wand cleaning a dark sofa cushion"/>
    <circle cx="1005" cy="448" r="124" fill="var(--white)"/>
    <circle cx="1005" cy="448" r="117" fill="url(#stain-tones)" role="img" aria-label="Photo: extraction tool lifting a stain from a cream carpet"/>

    <!-- guarantee seal -->
    <circle cx="1030" cy="620" r="86" fill="var(--deep-blue)"/>
    <circle cx="1030" cy="620" r="72" fill="var(--badge-dark)"/>
    <circle cx="1030" cy="620" r="40" fill="var(--white)"/>

    <!-- footer -->
    <path d="M452 720 H1160 V824 H476 Z" fill="var(--deep-blue)"/>
    <path d="M0 739 H450 L474 824 H0 Z" fill="var(--white)"/>
  </svg>

  <div class="brand">
    <div class="brand-mark"></div>
    <div class="brand-name">FIBERWAY</div>
  </div>

  <h1 class="headline">CARPET<br>CLEANING</h1>
  <p class="intro">We have been providing Carpet Cleaning Services for 40 years. With state-of-the-art industrial equipment &amp; out years of experience there is not mush we cannot get clean.</p>

  <ul class="services services-left">
    <li><svg viewBox="0 0 22 22"><circle cx="11" cy="11" r="9" fill="none" stroke="#fff" stroke-width="2"/><path d="M6.5 11.2l3 3 6-6" fill="none" stroke="#fff" stroke-width="2.2" stroke-linecap="round" stroke-linejoin="round"/></svg>RUG CLEANING</li>
    <li><svg viewBox="0 0 22 22"><circle cx="11" cy="11" r="9" fill="none" stroke="#fff" stroke-width="2"/><path d="M6.5 11.2l3 3 6-6" fill="none" stroke="#fff" stroke-width="2.2" stroke-linecap="round" stroke-linejoin="round"/></svg>BLEACH REPAIR</li>
    <li><svg viewBox="0 0 22 22"><circle cx="11" cy="11" r="9" fill="none" stroke="#fff" stroke-width="2"/><path d="M6.5 11.2l3 3 6-6" fill="none" stroke="#fff" stroke-width="2.2" stroke-linecap="round" stroke-linejoin="round"/></svg>UPHOLSTERY CLEANING</li>
    <li><svg viewBox="0 0 22 22"><circle cx="11" cy="11" r="9" fill="none" stroke="#fff" stroke-width="2"/><path d="M6.5 11.2l3 3 6-6" fill="none" stroke="#fff" stroke-width="2.2" stroke-linecap="round" stroke-linejoin="round"/></svg>PET STAIN AND SCENT REMOVAL</li>
  </ul>

  <ul class="services services-right">
    <li><svg viewBox="0 0 22 22"><circle cx="11" cy="11" r="9" fill="none" stroke="#fff" stroke-width="2"/><path d="M6.5 11.2l3 3 6-6" fill="none" stroke="#fff" stroke-width="2.2" stroke-linecap="round" stroke-linejoin="round"/></svg>BOAT, RV, PRIVATE PLANE<br>CARPET CLEANING</li>
    <li><svg viewBox="0 0 22 22"><circle cx="11" cy="11" r="9" fill="none" stroke="#fff" stroke-width="2"/><path d="M6.5 11.2l3 3 6-6" fill="none" stroke="#fff" stroke-width="2.2" stroke-linecap="round" stroke-linejoin="round"/></svg>CORRIDOR &amp; OUTDOOR<br>CARPET CLEANING</li>
  </ul>

  <p class="footer-tagline">RESIDENTIAL &amp; COMMERCIAL<br>CLEANING SERVICES</p>
  <p class="quote-cta">GET YOUR FREE<br>QUOTE TODAY !</p>
  <div class="cta-divider"></div>
  <p class="call"><span>CALL</span>(555) 318-4729</p>
  <p class="website">
    <svg viewBox="0 0 18 18"><g fill="none" stroke="#fff" stroke-width="1.5"><circle cx="9" cy="9" r="7.5"/><ellipse cx="9" cy="9" rx="3.2" ry="7.5"/><path d="M1.5 9h15"/></g></svg>
    WWW.FIBERWAYCARE.COM
  </p>
</main>
</body>
</html>
```